Creative Brief
Investment Banking Company Stationary
Business card, Letterhead, Envelope, Fax Cover
Professional
Daniyar Ospanturov
Managing Partner
27B Zheltoksan St,
Almaty, 050118
Kazakhstan
dospanturov@mailvero.kz
www.veltrafin.kz
The name of the company is Veltra Finance, LLP. In addition to the logo there should be text that includes the official name of the company.
I will need business cards for 3 other employees as well. Please message me for their relevant info.
Logo or blank

```html
<!DOCTYPE html>
<html lang="en">
<head>
<meta charset="utf-8">
<title>Veltra Finance — Stationery</title>
<link rel="stylesheet" href="https://fonts.googleapis.com/css2?family=Open+Sans:wght@400;600&display=swap">
<style>
:root{
  --blue:#1c4e8e;
  --blue-deep:#113a70;
  --blue-light:#3a6fb0;
  --ink:#333;
  --rule:#c9ced6;
  --paper:#fff;
  --dark:#1a1a1a;
  --grey:#7d7f84;
}
*{margin:0;padding:0;box-sizing:border-box}
html,body{width:1200px;height:504px;overflow:hidden;background:#fff}
body{position:relative;font-family:"Open Sans",sans-serif;color:var(--ink)}
.sheet{position:absolute;background:var(--paper);box-shadow:0 1px 4px rgba(0,0,0,.25)}

.brand-lockup{position:absolute;display:flex;align-items:center;gap:5px}
.brand-lockup.centered{left:0;right:0;justify-content:center}
.brand{font-family:"Open Sans",sans-serif;font-weight:600;color:var(--blue);white-space:nowrap}
.dot{display:block;border-radius:50%;background:var(--blue);flex:none}
.on-color .brand{color:#fff}
.on-color .dot{background:#fff}

.footer-band{position:absolute;left:0;right:0;height:12px;background:var(--blue);color:#fff;font-size:4px;display:flex;align-items:center;justify-content:space-around;padding:0 10px}

/* fax */
.fax{left:19px;top:7px;width:250px;height:485px}
.fax-title{position:absolute;right:22px;top:86px;font-size:15px;font-weight:600;color:#555;letter-spacing:1px}
.fax-form{position:absolute;left:14px;right:14px;top:108px;display:grid;grid-template-columns:1fr 1fr;gap:9px 14px;font-size:5px}
.fax-field{display:flex;align-items:flex-end;gap:4px}
.fax-field span{width:22px}
.fax-field i{flex:1;border-bottom:1px solid var(--rule);height:6px}
.fax-checks{position:absolute;left:14px;right:10px;top:184px;display:flex;justify-content:space-between;font-size:4.5px}
.fax-checks span::before{content:"";display:inline-block;width:5px;height:5px;border:1px solid #888;margin-right:2px;vertical-align:middle}
.fax-comments{position:absolute;left:14px;top:204px;font-size:5px}

/* envelope */
.envelope{left:288px;top:7px;width:420px;height:276px}
.envelope svg{position:absolute;left:0;top:0}

/* compliment slips */
.slip{width:360px}
.slip-a{left:341px;top:84px;height:199px}
.slip-b{left:341px;top:312px;height:168px}
.panel{position:absolute;top:0;bottom:0;background:radial-gradient(circle at 70% 40%,var(--blue-light),var(--blue) 55%,var(--blue-deep))}
.slip-a .panel{left:0;width:214px}
.slip-b .panel{right:0;width:190px}
.slip-address{position:absolute;font-size:4.5px;line-height:7px}
.slip-note{position:absolute;font-size:7px;letter-spacing:2px;text-transform:uppercase;color:var(--blue);white-space:nowrap}

/* letterhead */
.letterhead{left:725px;top:7px;width:367px;height:485px}

/* business cards */
.card{left:1108px;width:82px;height:78px;display:flex;flex-direction:column;justify-content:center;align-items:center;gap:4px}
.card .brand{font-size:6px}
.card .brand-lockup{position:static;gap:3px}
.card-white{top:12px;align-items:flex-start;padding-left:10px}
.card-white .person{font-size:4px;line-height:6px;color:var(--ink)}
.card-black{top:115px;background:radial-gradient(circle at 50% 40%,#444,var(--dark) 70%)}
.card-blue{top:216px;background:radial-gradient(circle at 50% 40%,var(--blue-light),var(--blue) 70%)}
.card-grey{top:316px;background:radial-gradient(circle at 50% 40%,#a3a5a9,var(--grey) 70%)}
.logo-solo{left:1110px;top:432px}
</style>
</head>
<body>

<section class="sheet fax">
  <div class="brand-lockup centered" style="top:22px">
    <span class="dot" style="width:6px;height:6px"></span>
    <span class="brand" style="font-size:9px">Veltra Finance</span>
  </div>
  <div class="fax-title">FAX</div>
  <div class="fax-form">
    <div class="fax-field"><span>To:</span><i></i></div>
    <div class="fax-field"><span>From:</span><i></i></div>
    <div class="fax-field"><span>Fax:</span><i></i></div>
    <div class="fax-field"><span>Pages:</span><i></i></div>
    <div class="fax-field"><span>Phone:</span><i></i></div>
    <div class="fax-field"><span>Date:</span><i></i></div>
    <div class="fax-field"><span>Re:</span><i></i></div>
    <div class="fax-field"><span>CC:</span><i></i></div>
  </div>
  <div class="fax-checks">
    <span>Urgent</span><span>For Review</span><span>Please Comment</span><span>Please Reply</span><span>Please Recycle</span>
  </div>
  <div class="fax-comments">Comments:</div>
  <div class="footer-band" style="top:455px">
    <span>27B Zheltoksan St, Almaty, 050118</span><span>T: +7 727 390 4412</span><span>office@veltrafin.kz</span><span>www.veltrafin.kz</span>
  </div>
</section>

<section class="sheet envelope">
  <svg width="420" height="276" viewBox="0 0 420 276" aria-hidden="true">
    <defs>
      <linearGradient id="flapShade" x1="0" y1="0" x2="0" y2="1">
        <stop offset="0" stop-color="#1c4e8e"/><stop offset="1" stop-color="#113a70"/>
      </linearGradient>
    </defs>
    <polygon points="0,0 420,0 420,20 230,130 190,130 0,20" fill="url(#flapShade)"/>
  </svg>
  <div class="brand-lockup centered on-color" style="top:36px">
    <span class="dot" style="width:5px;height:5px"></span>
    <span class="brand" style="font-size:7px">Veltra Finance</span>
  </div>
</section>

<section class="sheet slip slip-a">
  <div class="panel on-color">
    <div class="brand-lockup" style="left:14px;top:58px">
      <span class="dot" style="width:6px;height:6px"></span>
      <span class="brand" style="font-size:10px">Veltra Finance</span>
    </div>
    <div class="slip-address" style="left:14px;top:168px;color:#fff">27B Zheltoksan St, Almaty, 050118, Kazakhstan</div>
  </div>
  <div class="slip-note" style="left:232px;top:159px">With Compliments</div>
</section>

<section class="sheet slip slip-b">
  <div class="brand-lockup" style="left:18px;top:46px">
    <span class="dot" style="width:6px;height:6px"></span>
    <span class="brand" style="font-size:10px">Veltra Finance</span>
  </div>
  <div class="slip-address" style="left:18px;top:118px">27B Zheltoksan St, Almaty<br>050118, Kazakhstan</div>
  <div class="panel">
    <div class="slip-note" style="left:58px;top:136px;color:#fff">With Compliments</div>
  </div>
</section>

<section class="sheet letterhead">
  <div class="brand-lockup centered" style="top:26px">
    <span class="dot" style="width:6px;height:6px"></span>
    <span class="brand" style="font-size:10px">Veltra Finance</span>
  </div>
  <div class="footer-band" style="top:455px">
    <span>27B Zheltoksan St, Almaty, 050118, Kazakhstan</span><span>T: +7 727 390 4412</span><span>F: +7 727 390 4413</span><span>www.veltrafin.kz</span>
  </div>
</section>

<section class="sheet card card-white">
  <div class="brand-lockup">
    <span class="dot" style="width:4px;height:4px"></span>
    <span class="brand">Veltra Finance</span>
  </div>
  <div class="person">Daniyar Ospanturov<br>Managing Partner<br>dospanturov@mailvero.kz</div>
</section>
<section class="sheet card card-black on-color">
  <div class="brand-lockup"><span class="dot" style="width:4px;height:4px"></span><span class="brand">Veltra Finance</span></div>
</section>
<section class="sheet card card-blue on-color">
  <div class="brand-lockup"><span class="dot" style="width:4px;height:4px"></span><span class="brand">Veltra Finance</span></div>
</section>
<section class="sheet card card-grey on-color">
  <div class="brand-lockup"><span class="dot" style="width:4px;height:4px"></span><span class="brand">Veltra Finance</span></div>
</section>

<div class="brand-lockup logo-solo">
  <span class="dot" style="width:5px;height:5px"></span>
  <span class="brand" style="font-size:8px">Veltra Finance</span>
</div>

</body>
</html>
```